TKA Electricial Contracting Services

Hi guys, after a design for my small electrical company, have logo design files to be incorporated into the layout, the basic concept is electrical contracting services for residential, commercial, industrial & data services, image is clean clear and strong,

Card format is to have a nice clean logo on front,with maybe the Residential – commercial – industrial - data, followed with licensed & insured, followed by contact details on backside of the card.

Target Market(s)

Residential, commercial, industrial sectors.

Industry/Entity Type

Electrical

Contact Information for Business Card

TKA logo,
Residential – commercial – industrial - data
REC: 61372
Email: tka@poralink.net.au
Phone: 0458 203 719

Requirements
Must have
• Clean & strong design.
Nice to have
• If possible, I would like the logo colours inverted so the text is orange and the background is black on the front of the card, then the backside of the card be the reverse colour
Should not have
• No Sparks, lightning bolts,

```html
<!DOCTYPE html>
<html lang="en">
<head>
<meta charset="utf-8">
<title>TKA Electricial Contracting Services – Business Card</title>
<link rel="stylesheet" href="https://fonts.googleapis.com/css2?family=Open+Sans:wght@400;700&display=swap">
<style>
  :root {
    --backdrop: #474747;
    --card-black: #121212;
    --card-orange: #f28a2e;
    --brand-orange: #f2882a;
    --ink-black: #0d0d0d;
    --contact-grey: #9b9b9b;
  }
  * { margin: 0; padding: 0; box-sizing: border-box; }
  html, body { width: 1200px; height: 900px; overflow: hidden; }
  body {
    background: var(--backdrop);
    font-family: "Open Sans", Arial, sans-serif;
    position: relative;
  }
  .card {
    position: absolute;
    top: 218px;
    width: 278px;
    height: 458px;
    border-radius: 14px;
    text-align: center;
  }
  .card--front { left: 320px; background: var(--card-black); color: var(--brand-orange); }
  .card--back { left: 642px; background: var(--card-orange); color: var(--ink-black); }

  .brand {
    position: absolute;
    left: 0; right: 0;
    font-weight: 700;
    color: inherit;
  }
  .brand__name {
    display: block;
    font-size: 66px;
    line-height: 1;
    letter-spacing: 1px;
  }
  .brand__tagline {
    display: block;
    font-size: 13px;
    line-height: 1;
    margin-top: 6px;
  }
  .card--front .brand { top: 62px; }
  .card--back .brand { top: 176px; }

  .services {
    position: absolute;
    top: 181px;
    left: 0; right: 0;
    list-style: none;
    font-size: 13px;
    line-height: 17px;
    text-transform: uppercase;
  }
  .licence {
    position: absolute;
    top: 266px;
    left: 0; right: 0;
    font-size: 13px;
    line-height: 17px;
  }
  .contact {
    position: absolute;
    top: 375px;
    left: 0; right: 0;
    font-style: normal;
    font-size: 13.5px;
    line-height: 18px;
    color: var(--contact-grey);
  }
  .contact__line { display: flex; justify-content: center; align-items: center; gap: 5px; }
  .contact__icon { width: 10px; height: 10px; fill: var(--brand-orange); }
</style>
</head>
<body>
  <section class="card card--front" aria-label="Card front">
    <div class="brand">
      <span class="brand__name">TKA</span>
      <span class="brand__tagline">Tarrant Kelly Electrical</span>
    </div>
    <ul class="services">
      <li>Residential</li>
      <li>Commercial</li>
      <li>Industrial</li>
      <li>Data</li>
    </ul>
    <p class="licence">REC: 61372</p>
    <address class="contact">
      <div class="contact__line">
        <svg class="contact__icon" viewBox="0 0 10 10" aria-hidden="true">
          <path d="M1 3 Q1 1 5 1 Q9 1 9 3 L9 4 L7 4 L7 3 L3 3 L3 4 L1 4 Z M2.5 5 L3.5 4 L6.5 4 L7.5 5 L8.5 9 L1.5 9 Z"/>
        </svg>
        <span>0458 203 719</span>
      </div>
      <div class="contact__line">
        <svg class="contact__icon" viewBox="0 0 10 10" aria-hidden="true">
          <path d="M0.5 2 H9.5 V8.5 H0.5 Z" />
          <path d="M0.5 2 L5 5.5 L9.5 2" fill="none" stroke="#121212" stroke-width="0.9"/>
        </svg>
        <span>tka@poralink.net.au</span>
      </div>
    </address>
  </section>

  <section class="card card--back" aria-label="Card back">
    <div class="brand">
      <span class="brand__name">TKA</span>
      <span class="brand__tagline">Tarrant Kelly Electrical</span>
    </div>
  </section>
</body>
</html>
```